Book Cover Design 'Boundless Tide - Lessons In Inner Sovereignty'

I need to see pitches / artwork for a book cover for new book designed to start a new global spiritual movement and save humanity. The book merges science and spirituality and explains to the reader why they are an all powerful god.

```html
<!DOCTYPE html>
<html lang="en">
<head>
<meta charset="utf-8">
<title>Boundless Tide – Full Cover Spread</title>
<link rel="stylesheet" href="https://fonts.googleapis.com/css2?family=Barlow+Condensed:wght@600;700&family=Roboto:wght@300;400&family=Arimo:wght@400&display=swap">
<style>
  :root {
    --page-bg: #6b6b6b;
    --space-deep: #05060f;
    --space-navy: #0c1224;
    --nebula-orange: #c9692a;
    --nebula-amber: #e39a45;
    --nebula-teal: #3f9fb7;
    --nebula-cyan: #8fd6e6;
    --text-white: #ffffff;
    --text-soft: #e6e6e6;
    --accent-gold: #e8a23a;
    --fold-line: rgba(255,255,255,0.12);
  }
  * { box-sizing: border-box; margin: 0; padding: 0; }
  html, body { width: 1200px; height: 2182px; overflow: hidden; background: var(--page-bg); }
  .canvas { position: relative; width: 1200px; height: 2182px; }
  .cover-spread {
    position: absolute; left: 53px; top: 712px; width: 1094px; height: 757px;
    overflow: hidden; box-shadow: 0 10px 30px rgba(0,0,0,0.35);
    background: var(--space-deep);
  }
  .cover-art { position: absolute; inset: 0; }
  .cover-type { position: absolute; inset: 0; }
  .back-copy {
    position: absolute; font-family: "Arimo", sans-serif; color: var(--text-soft);
    font-size: 9.4px; line-height: 13.6px; text-align: justify;
  }
  .back-copy--blurb { left: 63px; top: 268px; width: 375px; }
  .back-copy--bio { left: 180px; top: 502px; width: 258px; }
  .author-heading {
    position: absolute; left: 187px; top: 479px; font-family: "Roboto", sans-serif;
    font-weight: 300; font-size: 18px; color: var(--accent-gold); letter-spacing: 0.2px;
  }
  .author-photo { position: absolute; left: 63px; top: 500px; width: 107px; height: 140px; background: var(--text-white); }
</style>
</head>
<body>
<div class="canvas">
  <section class="cover-spread">
    <svg class="cover-art" width="1094" height="757" viewBox="0 0 1094 757" role="img" aria-label="Deep-space nebula artwork in orange, amber and teal glowing clouds with scattered stars, wrapping across front cover and spine">
      <defs>
        <radialGradient id="nebulaCore" cx="0.78" cy="0.42" r="0.45">
          <stop offset="0" stop-color="var(--nebula-cyan)" stop-opacity="0.85"/>
          <stop offset="0.18" stop-color="var(--nebula-teal)" stop-opacity="0.8"/>
          <stop offset="0.45" stop-color="var(--nebula-orange)" stop-opacity="0.75"/>
          <stop offset="0.75" stop-color="#4a2412" stop-opacity="0.5"/>
          <stop offset="1" stop-color="var(--space-deep)" stop-opacity="0"/>
        </radialGradient>
        <radialGradient id="nebulaGlow" cx="0.72" cy="0.2" r="0.4">
          <stop offset="0" stop-color="var(--nebula-amber)" stop-opacity="0.5"/>
          <stop offset="1" stop-color="var(--nebula-amber)" stop-opacity="0"/>
        </radialGradient>
        <linearGradient id="spaceBase" x1="0" y1="0" x2="1" y2="0">
          <stop offset="0" stop-color="var(--space-deep)"/>
          <stop offset="0.45" stop-color="var(--space-navy)"/>
          <stop offset="1" stop-color="#1a140f"/>
        </linearGradient>
      </defs>
      <rect width="1094" height="757" fill="url(#spaceBase)"/>
      <rect width="1094" height="757" fill="url(#nebulaCore)"/>
      <rect width="1094" height="757" fill="url(#nebulaGlow)"/>
    </svg>

    <svg class="cover-type" width="1094" height="757" viewBox="0 0 1094 757">
      <line x1="500" y1="0" x2="500" y2="757" stroke="var(--fold-line)" stroke-width="1"/>
      <line x1="595" y1="0" x2="595" y2="757" stroke="var(--fold-line)" stroke-width="1"/>

      <g class="back-title" fill="var(--text-white)" font-family="'Barlow Condensed', sans-serif" font-weight="700" text-anchor="middle">
        <text x="255" y="177" font-size="72" textLength="218" lengthAdjust="spacingAndGlyphs">BOUNDLESS</text>
        <text x="255" y="233" font-size="72">TIDE</text>
      </g>
      <text x="255" y="257" fill="var(--text-white)" font-family="Roboto, sans-serif" font-weight="300" font-size="17" text-anchor="middle">Lessons In Inner Sovereignty</text>

      <g class="spine-type" fill="var(--text-white)">
        <text transform="translate(533,90) rotate(90)" font-family="'Barlow Condensed', sans-serif" font-weight="700" font-size="36" textLength="258" lengthAdjust="spacingAndGlyphs">BOUNDLESS TIDE</text>
        <text transform="translate(537,520) rotate(90)" font-family="Roboto, sans-serif" font-weight="300" font-size="25" textLength="190" lengthAdjust="spacingAndGlyphs">AUTHOR NAME</text>
      </g>

      <g class="front-title" fill="var(--text-white)" font-family="'Barlow Condensed', sans-serif" font-weight="700" text-anchor="middle" style="filter: drop-shadow(2px 3px 3px rgba(0,0,0,0.55));">
        <text x="845" y="307" font-size="134" textLength="415" lengthAdjust="spacingAndGlyphs">BOUNDLESS</text>
        <text x="845" y="417" font-size="134">TIDE</text>
      </g>
      <text x="845" y="457" fill="var(--text-white)" font-family="Roboto, sans-serif" font-weight="300" font-size="29" text-anchor="middle">Lessons In Inner Sovereignty</text>
      <text x="845" y="722" fill="var(--text-white)" font-family="Roboto, sans-serif" font-weight="300" font-size="31" text-anchor="middle">AUTHOR NAME</text>
    </svg>

    <p class="back-copy back-copy--blurb">Lorem Ipsum is simply dummy text of the printing and typesetting industry. Lorem Ipsum has been the industry's standard dummy text ever since the 1500s, when an unknown printer took a galley of type and scrambled it to make a type specimen book. It has survived not only five centuries, but also the leap into electronic typesetting, remaining essentially unchanged. It was popularised in the 1960s with the release of Linotext sheets containing Lorem Ipsum passages, and more recently with desktop publishing software like Verso Layout including versions of Lorem Ipsum.<br>Lorem Ipsum is simply dummy text of the printing and typesetting industry. Lorem Ipsum has been the industry's standard dummy text ever since the 1500s, when an unknown printer took a galley of type and scrambled it to make a type specimen book. It has survived not only five centuries, but also the leap into electronic typesetting, remaining essentially unchanged. It was popularised in the 1960s with the release of Linotext sheets containing Lorem Ipsum passages, and more recently with desktop publishing software like Verso Layout including versions of Lorem</p>

    <h2 class="author-heading">AUTHOR NAME</h2>
    <div class="author-photo" role="img" aria-label="Author portrait placeholder"></div>
    <p class="back-copy back-copy--bio">Lorem Ipsum is simply dummy text of the printing and typesetting industry. Lorem Ipsum has been the industry's standard dummy text ever since the 1500s, when an unknown printer took a galley of type and scrambled it to make a type specimen book. It has survived not only five centuries, but also the leap into electronic typesetting, remaining essentially unchanged. It was popularised in the 1960s with the release of Linotext sheets containing Lorem Ipsum passages, and more recently with desktop publishing software like Verso Layout including versions of Lorem Ipsum.</p>
  </section>
</div>
</body>
</html>
```